Business Card Design

Our Motto is "Protecting Australia's Underground Utilities"

We want the Southern Cross inside a shield I have attached the southern cross and our old shield design

Product description is: Vacuum Excavation & Utility Location
Wet & Dry Vacuum Loading
Confined Space Entry Specialists
High Pressure Cleaning

The Southern Cross in the shield must be blue and white. The Company name must be Coastal Pipeguard Services. The Green & Gold Shield logo I uploaded is my OLD logo design. Thank you

Target Market(s)

Civil Construction

Industry/Entity Type

Business

Contact Information for Business Card

Coastal Pipeguard Services Pty Ltd
Corey Halbrook(Director)
0413862975
coreyh@pipeguardco.com.au
A.B.N.52938470116

Colors
0456a3

Requirements
Must have
• Southern Cross inside a shield, Blue and white design on the Southern Cross shield.
Must say Coastal Pipeguard Services P/L

```html
<!DOCTYPE html>
<html lang="en">
<head>
<meta charset="utf-8">
<title>Coastal Pipeguard Services – Business Card</title>
<link href="https://fonts.googleapis.com/css2?family=Sorts+Mill+Goudy&display=swap" rel="stylesheet">
<style>
  :root {
    --backdrop: #4a4a4a;
    --card: #ffffff;
    --card-edge: #1a1a1a;
    --brand-ink: #0b0b0b;
    --brand-mark: #0456a3;
    --contact-ink: #4b4672;
  }
  * { margin: 0; padding: 0; box-sizing: border-box; }
  html, body {
    width: 890px;
    height: 1200px;
    overflow: hidden;
    background: var(--backdrop);
  }
  body {
    position: relative;
    font-family: "Sorts Mill Goudy", "Goudy Old Style", Georgia, serif;
  }
  .card {
    position: absolute;
    left: 47px;
    width: 806px;
    height: 473px;
    background: var(--card);
  }
  .card--front {
    top: 37px;
    border: 1px solid var(--card-edge);
  }
  .card--back { top: 687px; }

  .line {
    position: absolute;
    left: 0;
    right: 0;
    text-align: center;
    white-space: nowrap;
    line-height: 1;
  }

  /* Front face */
  .brand-mark {
    position: absolute;
    left: 50%;
    top: 150px;
    width: 56px;
    height: 56px;
    margin-left: -28px;
    background: var(--brand-mark);
  }
  .brand-name {
    color: var(--brand-ink);
    font-size: 39px;
    letter-spacing: 1.5px;
    text-transform: uppercase;
  }
  .brand-name--first { top: 268px; }
  .brand-name--second { top: 308px; }

  /* Back face */
  .contact { color: var(--contact-ink); }
  .contact__name { top: 100px; font-size: 40px; letter-spacing: 0.5px; }
  .contact__role { top: 144px; font-size: 24px; }
  .contact__phone { top: 260px; font-size: 32px; letter-spacing: 0.5px; }
  .contact__email { top: 299px; font-size: 32px; }
  .contact__abn { top: 341px; font-size: 24px; letter-spacing: 0.3px; }
</style>
</head>
<body>
  <section class="card card--front" aria-label="Card front">
    <div class="brand-mark" aria-hidden="true"></div>
    <p class="line brand-name brand-name--first">Coastal Pipeguard</p>
    <p class="line brand-name brand-name--second">Services</p>
  </section>

  <section class="card card--back contact" aria-label="Card back">
    <p class="line contact__name">Corey Halbrook</p>
    <p class="line contact__role">Director</p>
    <p class="line contact__phone">0413862975</p>
    <p class="line contact__email">coreyh@pipeguardco.com.au</p>
    <p class="line contact__abn">A.B.N.52938470116</p>
  </section>
</body>
</html>
```